Boutique Jewellery Card [UPDATED] Embossing and Foil

Hi Designers,

What will win you this competition is your input on making my card look very professional and classy

Just some overview information.

I am striving to be the most prestigious jeweller going around specialising in custom designed jewellery, engagement rings and repairs on a bigger budget.

I am spending a lot on the printing including thick cards, rounded corners, multi level embossing and foiling.

Front:

I want my entire logo on the front, which I will have embossed and foiled (source file included)
Optional: I also want a lower embossing of a repeating pattern which I am not sure on. I need YOUR input here

Back:

I need you to use your skills and experience to make my details look very important, professional and classy.

The details I need on the back are:

Marcus Feldwright
Your Jewellery Stylist

www.marcusfeldwright.com
0492 836 514
marcus@marcusfeldwright.com

The font MUST match the font/style used in the logo.
Everything else including layout, whether my logo is on the back etc, engrave/endent, foiling etc is what I need your input for
Updates

Project Deadline Extended Reason: I was a bit slow and out of action at the start, but we're almost there, just need a few more days to finalize Added Sunday, November 16, 2014

Target Market(s)

25 - 80 year olds. Fashion concious. Wealthy

Industry/Entity Type

Printing

Contact Information for Business Card

Marcus Feldwright
Your Jewellery Stylist

0492 836 514
marcus@marcusfeldwright.com
www.marcusfeldwright.com
- facebook and instagram logo's

Requirements
Must have
• Must use the font from my logo on the back, or very similar
• My logo on the front
• My details on the back must be the centre of attention, my logo can still be there but is less important.
• Back must include the facebook and instagram logo's
Nice to have
• repeating pattern or monogram

```html
<!DOCTYPE html>
<html lang="en">
<head>
<meta charset="utf-8">
<title>Marcus Feldwright — Business Card</title>
<link rel="stylesheet" href="https://fonts.googleapis.com/css2?family=Saira+Semi+Condensed:wght@300;600&display=swap">
<style>
  :root {
    --backdrop: #e4e4e6;
    --charcoal: #48464a;
    --charcoal-text: #5e5c61;
    --paper: #ffffff;
    --ink: #3d3b3f;
    --light-ink: #f2f2f2;
  }
  * { margin: 0; padding: 0; box-sizing: border-box; }
  html, body {
    width: 1200px;
    height: 1192px;
    overflow: hidden;
    background: var(--backdrop);
    font-family: "Saira Semi Condensed", "Arial Narrow", sans-serif;
  }
  .card {
    position: absolute;
    left: 160px;
    width: 880px;
    height: 503px;
    border-radius: 14px;
    overflow: hidden;
    box-shadow: 0 6px 18px rgba(0,0,0,0.12);
  }
  .card--front { top: 60px; background: var(--charcoal); }
  .card--back { top: 629px; background: var(--paper); }

  /* Front */
  .front-mark {
    position: absolute;
    left: 50%;
    top: 70px;
    width: 120px;
    height: 120px;
    margin-left: -60px;
    border: 5px solid var(--charcoal-text);
    border-radius: 50%;
  }
  .front-name,
  .front-tagline,
  .front-region {
    position: absolute;
    left: 0;
    width: 100%;
    text-align: center;
    white-space: nowrap;
    font-weight: 300;
    color: var(--charcoal-text);
    text-transform: uppercase;
    line-height: 1;
  }
  .front-name {
    top: 226px;
    font-size: 52px;
    letter-spacing: 10px;
  }
  .front-tagline {
    top: 300px;
    font-size: 30px;
    letter-spacing: 12px;
  }
  .front-region {
    top: 350px;
    font-size: 18px;
    letter-spacing: 12px;
  }

  /* Back */
  .back-band {
    position: absolute;
    left: 0;
    bottom: 0;
    width: 100%;
    height: 218px;
    background: var(--charcoal);
  }
  .back-identity {
    position: absolute;
    left: 330px;
    top: 196px;
    color: var(--ink);
    text-transform: uppercase;
    white-space: nowrap;
  }
  .back-name {
    font-weight: 600;
    font-size: 36px;
    letter-spacing: 5px;
    line-height: 1;
  }
  .back-role {
    margin-top: 8px;
    font-weight: 600;
    font-size: 16px;
    letter-spacing: 3px;
    text-align: right;
  }
  .back-contact {
    position: absolute;
    left: 330px;
    top: 318px;
    list-style: none;
    color: var(--light-ink);
    font-weight: 300;
    font-size: 19px;
    letter-spacing: 3px;
    line-height: 1.45;
    text-transform: uppercase;
    white-space: nowrap;
  }
</style>
</head>
<body>
  <section class="card card--front" aria-label="Card front">
    <div class="front-mark"></div>
    <h1 class="front-name">Marcus Feldwright</h1>
    <p class="front-tagline">Designer Jewellery</p>
    <p class="front-region">Australia</p>
  </section>

  <section class="card card--back" aria-label="Card back">
    <div class="back-identity">
      <h2 class="back-name">Marcus Feldwright</h2>
      <p class="back-role">Your Jewellery Stylist</p>
    </div>
    <div class="back-band"></div>
    <ul class="back-contact">
      <li>0492 836 514</li>
      <li>marcus@marcusfeldwright.com</li>
      <li>www.marcusfeldwright.com</li>
    </ul>
  </section>
</body>
</html>
```